Stylish Business Cards Wanted

- DOUBLE SIDED Design Required -

High end, edgy cards for a corporate and personal stylist. Must include logo,
Name: Belinda Forsey
Title: Director and Stylist
telephone : +61 8 8217 4592
email: belinda@thegarbledger.example
website: thegarbledger.example
Tag: Corporate Workwear & Uniform Specialist | Personal Stylist
Would like nice icons for telephone, email, website

Target Market(s)

Businesses wanting stylish uniforms, people wanting stylish wardrobes

Industry/Entity Type

Corporate Workwear Stylist

Contact Information for Business Card

I would like black, white and gold foiling incorporated in the design - possibly a touch of the other colours on my branding guide attached Name: Belinda Forsey Title: Director and Stylist telephone : +61 8 8217 4592 email: belinda@thegarbledger.example website: thegarbledger.example Tag: Corporate Workwear & Uniform Specialist | Personal Stylist Would like nice icons for telephone, email, website

Font styles to use
Other font styles liked:
• Raleway

Colors

Designer to choose colors to be used in the design.

Requirements
Must have
• Gold foil accents

```html
<!DOCTYPE html>
<html lang="en">
<head>
<meta charset="utf-8">
<title>The Garb Ledger — Business Cards</title>
<link href="https://fonts.googleapis.com/css2?family=Roboto:wght@400;500;700&family=Courgette&display=swap" rel="stylesheet">
<style>
  :root {
    --backdrop: #2f2f31;
    --backdrop-edge: #1c1c1e;
    --card: #1d1d20;
    --gold: #d9ac2f;
    --gold-light: #f3d36a;
    --gold-deep: #a9801c;
    --white: #f4f4f4;
    --accent-pink: #c2186b;
  }
  * { margin: 0; padding: 0; box-sizing: border-box; }
  html, body {
    width: 799px;
    height: 1200px;
    overflow: hidden;
  }
  body {
    background: radial-gradient(ellipse at 50% 40%, var(--backdrop) 0%, var(--backdrop-edge) 100%);
    font-family: "Roboto", Arial, sans-serif;
    position: relative;
  }
  .card {
    position: absolute;
    left: 100px;
    width: 600px;
    height: 343px;
    background: var(--card);
    border-radius: 22px;
    box-shadow: 0 14px 30px rgba(0,0,0,0.55);
    overflow: hidden;
  }
  .card--front { top: 128px; }
  .card--back { top: 728px; }

  /* Front */
  .front-brand {
    position: absolute;
    inset: 0;
    display: flex;
    flex-direction: column;
    align-items: center;
    justify-content: center;
    gap: 6px;
  }
  .brand-name {
    font-family: "Roboto", Arial, sans-serif;
    font-weight: 700;
    text-transform: uppercase;
    letter-spacing: 0.14em;
  }
  .front-brand .brand-name {
    color: var(--gold);
    font-size: 44px;
  }
  .front-brand .brand-mark {
    width: 14px;
    height: 14px;
    background: var(--gold);
  }

  /* Back */
  .holder-name {
    position: absolute;
    left: 40px;
    top: 34px;
    font-family: "Courgette", cursive;
    font-size: 27px;
    color: var(--gold);
  }
  .holder-title {
    position: absolute;
    left: 40px;
    top: 76px;
    font-size: 12.5px;
    color: var(--white);
  }
  .contact-list {
    position: absolute;
    left: 40px;
    top: 110px;
    list-style: none;
  }
  .contact-item {
    display: flex;
    align-items: center;
    gap: 10px;
    height: 24px;
    font-size: 14px;
    color: var(--white);
  }
  .contact-item svg {
    width: 13px;
    height: 13px;
    flex: none;
  }
  .divider {
    position: absolute;
    left: 0;
    top: 0;
    width: 600px;
    height: 343px;
  }
  .back-brand {
    position: absolute;
    right: 34px;
    top: 58px;
    display: flex;
    align-items: center;
    gap: 8px;
  }
  .back-brand .brand-name {
    color: var(--white);
    font-size: 22px;
  }
  .back-brand .brand-mark {
    width: 9px;
    height: 9px;
    background: var(--white);
  }
  .services {
    position: absolute;
    right: 34px;
    bottom: 26px;
    list-style: none;
    text-align: right;
  }
  .service {
    font-size: 14px;
    line-height: 21px;
    color: var(--white);
  }
  .service::after {
    content: "«";
    color: var(--accent-pink);
    font-size: 12px;
    margin-left: 7px;
  }
</style>
</head>
<body>

  <section class="card card--front" aria-label="Business card front">
    <div class="front-brand">
      <span class="brand-name">The Garb Ledger</span>
      <span class="brand-mark"></span>
    </div>
  </section>

  <section class="card card--back" aria-label="Business card back">
    <p class="holder-name">Belinda Forsey</p>
    <p class="holder-title">Director and Stylist</p>

    <ul class="contact-list">
      <li class="contact-item">
        <svg viewBox="0 0 16 16" aria-hidden="true">
          <circle cx="8" cy="8" r="7" fill="none" stroke="var(--gold)" stroke-width="1.4"/>
          <path d="M5.6 4.6 L6.8 4.4 L7.4 6.2 L6.6 6.9 Q7.4 8.6 9.1 9.4 L9.8 8.6 L11.6 9.2 L11.4 10.4 Q10.9 11.4 9.6 11.2 Q5.2 10.2 4.8 6 Q4.8 5 5.6 4.6 Z" fill="var(--gold)"/>
        </svg>
        +61 8 8217 4592
      </li>
      <li class="contact-item">
        <svg viewBox="0 0 16 16" aria-hidden="true">
          <rect x="1.5" y="3.5" width="13" height="9" fill="none" stroke="var(--gold)" stroke-width="1.4"/>
          <path d="M1.5 3.5 L8 9 L14.5 3.5" fill="none" stroke="var(--gold)" stroke-width="1.4"/>
        </svg>
        belinda@thegarbledger.example
      </li>
      <li class="contact-item">
        <svg viewBox="0 0 16 16" aria-hidden="true">
          <circle cx="8" cy="8" r="6.5" fill="none" stroke="var(--gold)" stroke-width="1.3"/>
          <ellipse cx="8" cy="8" rx="2.8" ry="6.5" fill="none" stroke="var(--gold)" stroke-width="1.1"/>
          <path d="M1.5 8 H14.5 M2.6 4.6 H13.4 M2.6 11.4 H13.4" stroke="var(--gold)" stroke-width="1.1"/>
        </svg>
        www.thegarbledger.example
      </li>
    </ul>

    <svg class="divider" viewBox="0 0 600 343" aria-hidden="true">
      <path d="M40 196 H300 C335 196 330 232 370 232 H570" fill="none" stroke="var(--gold)" stroke-width="1.4"/>
    </svg>

    <div class="back-brand">
      <span class="brand-name">The Garb Ledger</span>
      <span class="brand-mark"></span>
    </div>

    <ul class="services">
      <li class="service">Personal Stylist</li>
      <li class="service">Corporate Workwear</li>
      <li class="service">&amp; Uniform Specialist</li>
    </ul>
  </section>

</body>
</html>
```